Stride42! Brochure

We need a bi-fold 8.5 inches by 11 inches standard size. The outline is attached with key sections included. The design needs to fit our brand standard and needs to be editable. We are requesting two rounds of edits. Photos can be provided to the selected designer to use. We are open to gatefold designs as well. The website for design reference is https://www.stride42.example/ . I will include the color palate and brochure content in the uploaded files.

```html
<!DOCTYPE html>
<html lang="en">
<head>
<meta charset="utf-8">
<title>Stride42! Brochure – Inside Spread</title>
<link href="https://fonts.googleapis.com/css2?family=Bitter:ital,wght@0,400;0,700;0,800;1,400&display=swap" rel="stylesheet">
<style>
  :root {
    --backdrop: #c9c9c9;
    --paper: #f6f6f5;
    --ink: #2b2f33;
    --navy: #1f3447;
    --orange: #e0744a;
    --orange-soft: #e99672;
    --teal: #235a77;
    --photo-blue: #2f4fb8;
    --photo-sand: #e8d49a;
  }
  * { box-sizing: border-box; margin: 0; padding: 0; }
  html, body { width: 1200px; height: 833px; overflow: hidden; }
  body {
    background: var(--backdrop);
    font-family: "Bitter", Georgia, serif;
    color: var(--ink);
    display: flex;
    align-items: center;
    justify-content: center;
  }
  .spread {
    display: flex;
    width: 1080px;
    height: 720px;
    box-shadow: 0 10px 30px rgba(0,0,0,.18);
  }
  .page {
    position: relative;
    width: 540px;
    height: 720px;
    background: var(--paper);
    overflow: hidden;
  }
  .page--left { box-shadow: inset -14px 0 18px -14px rgba(0,0,0,.18); }
  .page--right { box-shadow: inset 14px 0 18px -14px rgba(0,0,0,.14); }
  .page__art { position: absolute; inset: 0; width: 540px; height: 720px; }
  .page__content { position: absolute; }
  .page--left .page__content { left: 62px; top: 345px; width: 420px; }
  .page--right .page__content { left: 54px; top: 252px; width: 432px; }
  .section-title {
    font-weight: 800;
    font-style: italic;
    font-size: 17px;
    color: var(--navy);
    letter-spacing: .2px;
  }
  .section-title::after {
    content: "";
    display: block;
    width: 16px;
    height: 3px;
    margin: 3px 0 8px;
    background: var(--orange);
  }
  .section + .section { margin-top: 16px; }
  .body-copy {
    font-size: 10px;
    line-height: 1.42;
    margin-bottom: 7px;
  }
  .service-list { list-style: none; font-size: 10px; line-height: 1.45; font-weight: 700; color: var(--navy); }
  .service-list__label { color: var(--orange); font-style: italic; font-weight: 400; }
  .stat-list { list-style: none; font-size: 10px; line-height: 1.45; font-weight: 700; color: var(--navy); }
  .stat-list li { position: relative; padding-left: 14px; }
  .stat-list li::before {
    content: "";
    position: absolute;
    left: 1px; top: 3px;
    width: 7px; height: 4px;
    border-left: 1.6px solid var(--orange);
    border-bottom: 1.6px solid var(--orange);
    transform: rotate(-45deg);
  }
</style>
</head>
<body>
  <main class="spread">
    <section class="page page--left">
      <svg class="page__art" viewBox="0 0 540 720">
        <defs>
          <linearGradient id="grad-graduates" x1="0" y1="0" x2="0" y2="1">
            <stop offset="0" stop-color="var(--photo-sand)"/>
            <stop offset=".35" stop-color="#c9b27a"/>
            <stop offset=".55" stop-color="var(--photo-blue)"/>
            <stop offset="1" stop-color="#243f96"/>
          </linearGradient>
        </defs>
        <path role="img" aria-label="Photo: group of smiling graduates in blue caps and gowns in front of a school building"
              d="M0 0 H540 V318 Q300 268 0 282 Z" fill="url(#grad-graduates)"/>
        <path aria-hidden="true" d="M0 282 Q300 268 540 318 V326 Q300 278 0 286 Z" fill="var(--orange-soft)"/>
        <path aria-hidden="true" d="M0 605 L150 720 H0 Z" fill="var(--orange)"/>
      </svg>
      <div class="page__content">
        <div class="section">
          <h2 class="section-title">Mission</h2>
          <p class="body-copy">Our mission at Stride42! is to increase the number of college graduates, creating a generation of young adults prepared to take on today's most challenging jobs and earn a living wage for a happy life.</p>
          <p class="body-copy">We don't have a one-size-fits-all approach. Instead, we sit down with every school we work with to identify their individual challenges and create a plan that has a combination of consulting, professional development, program design and performance management.</p>
        </div>
        <div class="section">
          <h2 class="section-title">Who We Are</h2>
          <p class="body-copy">Stride42! officially launched in April 2018, but our passion for helping schools and students started long before that. In fact, founder Dana Whitfield has been working on college prep since 2006, coaching over 40 college academic counselors and managing a staff of over 10 high school counselors. Stride42! is the culmination of all that experience in a single, streamlined business model that can help more schools and students.</p>
        </div>
      </div>
    </section>

    <section class="page page--right">
      <svg class="page__art" viewBox="0 0 540 720">
        <defs>
          <linearGradient id="grad-lockers" x1="0" y1="0" x2="1" y2="0">
            <stop offset="0" stop-color="#d9dde0"/>
            <stop offset=".4" stop-color="#6b5a4a"/>
            <stop offset=".6" stop-color="#2c3d66"/>
            <stop offset="1" stop-color="#efe3b8"/>
          </linearGradient>
        </defs>
        <path role="img" aria-label="Photo: smiling student with curly hair standing at school lockers in a hallway"
              d="M0 0 H540 V196 Q260 160 0 184 Z" fill="url(#grad-lockers)"/>
        <path aria-hidden="true" d="M0 184 Q260 160 540 196 V203 Q260 167 0 189 Z" fill="#ffffff"/>
        <path aria-hidden="true" d="M0 189 Q260 167 540 203 V226 Q260 186 0 204 Z" fill="var(--orange)"/>
        <path aria-hidden="true" d="M540 625 V720 H385 Z" fill="var(--teal)"/>
      </svg>
      <div class="page__content">
        <div class="section">
          <h2 class="section-title">What We Do</h2>
          <p class="body-copy">Stride42! provides consulting, professional development, program design and performance management technology to ensure high schools and colleges achieve strong graduation rates and postsecondary success.</p>
          <p class="body-copy">Every school, counselor and student we work with is evaluated based on their individual needs. Our comprehensive needs assessment helps us design a program around you and your students' needs.</p>
          <ul class="service-list">
            <li><span class="service-list__label">Hire –</span> We can hire the right counseling staff for you.</li>
            <li><span class="service-list__label">Train –</span> We can train your existing counseling staff.</li>
            <li><span class="service-list__label">Coach –</span> We can provide ongoing coaching for your staff.</li>
            <li><span class="service-list__label">Track –</span> We can track the results for your program including graduation rates, matriculation and persistence.</li>
          </ul>
        </div>
        <div class="section">
          <h2 class="section-title">Who We Serve</h2>
          <p class="body-copy">There are lots of college prep programs in the US. But few are built to serve minority and low socioeconomic populations in the Midwest and Southeast. And even fewer have the successful track record like Stride42!</p>
          <ul class="stat-list">
            <li>15% of students who entered high school in 2017 are not expected to graduate.</li>
            <li>25% of minority students who entered high school in 2017 are not expected to graduate.</li>
            <li>43% of students who do graduate will not immediately enroll in college.</li>
            <li>60% of students who do enroll in college will never finish with a degree.</li>
          </ul>
        </div>
      </div>
    </section>
  </main>
</body>
</html>
```